Business Card Design Project

We are an incubator company that helps young entrepreneur to launch new ideas into the market. We will be targeting investors or likewise; Angels, young entrepreneurs and technopreneurs.

Our logo is being tasked by artflockly to design, therefore there is no logo for now.
You can us Lanternfold Pte Ltd as the logo for the time being.

Please let us have some versions of modern and yet professional designs; for words, you can indicate e.g (address), (Title)

thanks

Target Market(s)

young entrepreneurs
angels, investors

Industry/Entity Type

Business

Colors
3176b5
ffffff

Requirements
Must have
• able to project out our name; Lanternfold
Should not have
• Nothing childish or cartoon

```html
<!DOCTYPE html>
<html lang="en">
<head>
<meta charset="utf-8">
<title>Lanternfold Pte Ltd – Business Card</title>
<link href="https://fonts.googleapis.com/css2?family=Saira+Semi+Condensed:wght@400;600&display=swap" rel="stylesheet">
<style>
  :root {
    --stage: #e4e2e7;
    --paper-light: #ffffff;
    --paper-shade: #e3e3e3;
    --brand: #3176b5;
    --brand-light: #27a2de;
    --brand-mid: #1c7cc4;
    --brand-deep: #1a4f8c;
    --ink: #1f55a3;
    --ink-soft: #2a6fb5;
  }
  * { margin: 0; padding: 0; box-sizing: border-box; }
  html, body {
    width: 1200px; height: 900px; overflow: hidden;
    background: var(--stage);
    font-family: "Saira Semi Condensed", Arial, sans-serif;
  }
  .card {
    position: absolute; top: 300px;
    width: 531px; height: 300px;
    overflow: hidden;
    box-shadow: 0 6px 14px rgba(0,0,0,.22);
  }
  .card--front { left: 50px; }
  .card--back { left: 619px; }
  .card__art { position: absolute; inset: 0; width: 100%; height: 100%; }

  .brand {
    position: absolute; left: 0; width: 445px; top: 78px;
    display: flex; flex-direction: column; align-items: center;
    color: var(--ink);
  }
  .brand__mark {
    width: 64px; height: 64px; background: var(--ink); margin-bottom: 18px;
  }
  .brand__name {
    font-weight: 600; font-size: 38px; line-height: 1;
    letter-spacing: 1px; text-transform: uppercase;
    white-space: nowrap;
  }
  .brand__tagline {
    font-weight: 600; font-size: 9.5px; letter-spacing: 2.2px;
    text-transform: uppercase; margin-top: 4px; margin-left: 40px;
    white-space: nowrap;
  }

  .contact {
    position: absolute; left: 322px; top: 130px;
    color: var(--ink-soft);
  }
  .contact__name {
    font-size: 27px; font-weight: 400; line-height: 1; margin-bottom: 12px;
    white-space: nowrap;
  }
  .contact__list { list-style: none; }
  .contact__item {
    display: flex; align-items: center; gap: 12px;
    font-size: 11.5px; height: 19px; white-space: nowrap;
  }
  .contact__icon { width: 12px; height: 12px; fill: var(--ink-soft); flex: none; }
</style>
</head>
<body>

<section class="card card--front" aria-label="Business card front">
  <svg class="card__art" viewBox="0 0 425 240" preserveAspectRatio="none">
    <defs>
      <linearGradient id="paper" x1="0" y1="0" x2="1" y2="1">
        <stop offset="0" stop-color="var(--paper-light)"/>
        <stop offset="1" stop-color="var(--paper-shade)"/>
      </linearGradient>
      <linearGradient id="frontCorner" x1="0" y1="0" x2="0" y2="1">
        <stop offset="0" stop-color="var(--brand-light)"/>
        <stop offset="1" stop-color="var(--brand)"/>
      </linearGradient>
      <linearGradient id="frontBand" x1="0" y1="0" x2="1" y2="0">
        <stop offset="0" stop-color="var(--brand-mid)"/>
        <stop offset="1" stop-color="var(--brand-deep)"/>
      </linearGradient>
    </defs>
    <rect width="425" height="240" fill="url(#paper)"/>
    <polygon points="0,216 379,165 425,240 0,240" fill="url(#frontBand)"/>
    <polygon points="278,0 425,0 425,240" fill="url(#frontCorner)"/>
  </svg>
  <div class="brand">
    <span class="brand__mark" aria-hidden="true"></span>
    <span class="brand__name">Lanternfold</span>
    <span class="brand__tagline">Launching Ideas Into Market</span>
  </div>
</section>

<section class="card card--back" aria-label="Business card back">
  <svg class="card__art" viewBox="0 0 425 240" preserveAspectRatio="none">
    <defs>
      <linearGradient id="backSky" x1="0" y1="0" x2="1" y2="0">
        <stop offset="0" stop-color="var(--brand-mid)"/>
        <stop offset="1" stop-color="var(--brand-light)"/>
      </linearGradient>
      <linearGradient id="backPaper" x1="0" y1="0" x2="1" y2="1">
        <stop offset="0" stop-color="var(--paper-shade)"/>
        <stop offset="1" stop-color="var(--paper-light)"/>
      </linearGradient>
      <linearGradient id="backBand" x1="0" y1="0" x2="1" y2="0">
        <stop offset="0" stop-color="var(--brand-deep)"/>
        <stop offset="1" stop-color="var(--brand)"/>
      </linearGradient>
    </defs>
    <rect width="425" height="240" fill="url(#backSky)"/>
    <polygon points="95,192 425,0 425,240" fill="url(#backPaper)"/>
    <polygon points="0,205 95,192 425,240 0,240" fill="url(#backBand)"/>
  </svg>
  <div class="contact">
    <p class="contact__name">Name Surname</p>
    <ul class="contact__list">
      <li class="contact__item">
        <svg class="contact__icon" viewBox="0 0 24 24"><path d="M6.6 10.8a15 15 0 0 0 6.6 6.6l2.2-2.2c.3-.3.7-.4 1-.2 1.1.4 2.3.6 3.6.6.6 0 1 .4 1 1V20c0 .6-.4 1-1 1A17 17 0 0 1 3 4c0-.6.4-1 1-1h3.5c.6 0 1 .4 1 1 0 1.3.2 2.5.6 3.6.1.3 0 .7-.2 1z"/></svg>
        000 000 000
      </li>
      <li class="contact__item">
        <svg class="contact__icon" viewBox="0 0 24 24"><path d="M7 1h10a2 2 0 0 1 2 2v18a2 2 0 0 1-2 2H7a2 2 0 0 1-2-2V3a2 2 0 0 1 2-2zm0 3v14h10V4zm5 15.5a1.2 1.2 0 1 0 0 2.4 1.2 1.2 0 0 0 0-2.4z"/></svg>
        000 000 000
      </li>
      <li class="contact__item">
        <svg class="contact__icon" viewBox="0 0 24 24"><path d="M2 5h20v14H2zm2 2v.5l8 5 8-5V7zm0 2.8V17h16V9.8l-8 5z"/></svg>
        email@website.com
      </li>
      <li class="contact__item">
        <svg class="contact__icon" viewBox="0 0 24 24"><path d="M12 2a10 10 0 1 0 0 20 10 10 0 0 0 0-20zm6.9 6h-3a15 15 0 0 0-1.3-3.9A8 8 0 0 1 18.9 8zM12 4c.8 1.2 1.5 2.5 1.9 4h-3.8c.4-1.5 1.1-2.800 1.9-4zM4.3 14a8 8 0 0 1 0-4h3.4a16 16 0 0 0 0 4zm.8 2h3a15 15 0 0 0 1.3 3.9A8 8 0 0 1 5.1 16zm3-8h-3a8 8 0 0 1 4.3-3.9C8.9 5.3 8.4 6.6 8.1 8zM12 20c-.8-1.2-1.5-2.5-1.9-4h3.8c-.4 1.5-1.1 2.8-1.9 4zm2.3-6H9.7a14 14 0 0 1 0-4h4.6a14 14 0 0 1 0 4zm.3 5.9c.6-1.2 1-2.5 1.3-3.9h3a8 8 0 0 1-4.3 3.9zm1.7-5.9a16 16 0 0 0 0-4h3.4a8 8 0 0 1 0 4z"/></svg>
        www.website.com
      </li>
    </ul>
  </div>
</section>

</body>
</html>
```